MOV Promotional flyer for students

We're looking for an 8.5" x 11" flyer that will be distributed to schools. Please see language to include in attached files.

Target Market(s)

The parents and teachers of high school students

Industry/Entity Type

Mental health

Other font styles liked:
• Monserrat and Roboto Slab

Requirements
Must have
• See attached pdf for language to be included on the flyer. Please use the color palette from our website: www.lumemov.tv. Please include some imagery of students. Please ensure the
Nice to have
• Feel free to use any of the graphics provided. See our website for our brand look & feel: www.lumemov.tv

```html
<!DOCTYPE html>
<html lang="en">
<head>
<meta charset="utf-8">
<title>Fundraise with MOV – Flyer</title>
<link href="https://fonts.googleapis.com/css2?family=Montserrat:wght@500;600;700;800;900&display=swap" rel="stylesheet">
<style>
  :root {
    --page-bg: #d9d9d9;
    --paper: #e9eff3;
    --orange: #f0862a;
    --blue-dark: #266a93;
    --blue-light: #8fbeda;
    --ink: #2e6585;
    --white: #ffffff;
  }
  * { box-sizing: border-box; margin: 0; padding: 0; }
  html, body {
    width: 1200px; height: 986px; overflow: hidden;
    background: var(--page-bg);
    font-family: "Montserrat", Arial, sans-serif;
  }
  .flyer {
    position: absolute; left: 244px; top: 33px;
    width: 712px; height: 920px;
    background: var(--paper);
    overflow: hidden;
  }
  .flyer > * { position: absolute; }
  .top-shapes { left: 0; top: 0; width: 712px; height: 300px; }
  .headline {
    left: 56px; top: 118px;
    color: var(--white);
    font-weight: 900; font-size: 60px; line-height: 1.02;
    text-transform: uppercase; letter-spacing: 0.5px;
  }
  .brand-mark {
    right: 34px; top: 76px;
    width: 156px; height: 156px; border-radius: 50%;
    background: var(--blue-dark);
    display: flex; align-items: center; justify-content: center;
    color: var(--white); font-weight: 800; font-size: 48px;
  }
  .proceeds-band {
    left: 0; top: 292px; width: 470px; height: 118px;
    background: var(--blue-dark);
    padding: 22px 0 0 50px;
    color: var(--white); font-weight: 800; font-size: 21px; line-height: 1.2;
    text-transform: uppercase;
  }
  .accent-blob {
    width: 300px; height: 300px; border-radius: 50%;
    left: 470px; top: 560px; background: var(--blue-dark);
  }
  .students-photo {
    left: 318px; top: 262px; width: 400px; height: 400px; border-radius: 50%;
    border: 7px solid var(--blue-light);
    background: linear-gradient(160deg, #e8d9c6 0%, #b88e72 35%, #4f6ea8 65%, #7c97c0 100%);
  }
  .quote {
    left: 36px; top: 458px; width: 274px;
    color: var(--blue-light); font-weight: 900; font-size: 23px; line-height: 1.2;
    text-transform: uppercase; text-align: right;
    z-index: 2;
  }
  .quote-mark {
    font-size: 96px; line-height: 1; font-weight: 900; color: var(--blue-light);
    z-index: 3;
  }
  .quote-open { left: 30px; top: 408px; }
  .quote-close { left: 262px; top: 538px; }
  .side-band { left: 0; top: 640px; width: 130px; height: 280px; background: var(--blue-dark); }
  .side-circle {
    left: 120px; top: 600px; width: 220px; height: 220px; border-radius: 50%;
    background: var(--blue-light);
  }
  .student-photo {
    left: 40px; top: 620px; width: 300px; height: 300px;
    border-radius: 140px 140px 0 0;
    background: linear-gradient(180deg, #c9a58a 0%, #8a6a58 40%, #c43a2e 70%, #7f7f86 100%);
  }
  .about-box {
    left: 316px; top: 688px; width: 374px; height: 176px;
    background: var(--orange); border-radius: 28px;
    padding: 20px 22px;
    color: var(--white); font-weight: 700; font-size: 15.5px; line-height: 1.32;
    text-align: center;
  }
  .site-url {
    left: 316px; top: 880px; width: 374px; text-align: center;
    color: var(--ink); font-weight: 500; font-size: 21px; letter-spacing: 1px;
    text-transform: uppercase;
  }
</style>
</head>
<body>
  <main class="flyer">
    <svg class="top-shapes" viewBox="0 0 712 300" aria-hidden="true">
      <rect x="0" y="0" width="712" height="300" fill="var(--orange)"/>
      <circle cx="170" cy="-10" r="100" fill="var(--blue-light)"/>
      <circle cx="40" cy="30" r="95" fill="var(--blue-dark)"/>
    </svg>

    <h1 class="headline">Fundraise<br>with MOV</h1>
    <div class="brand-mark">MOV</div>

    <p class="proceeds-band">50% of all proceeds<br>go back to your<br>school</p>

    <div class="accent-blob" aria-hidden="true"></div>
    <div class="students-photo" role="img" aria-label="Photo of two smiling high school students holding notebooks outside a school building"></div>

    <div class="side-band" aria-hidden="true"></div>
    <div class="side-circle" aria-hidden="true"></div>
    <div class="student-photo" role="img" aria-label="Photo of a smiling student in a plaid shirt pointing forward"></div>

    <span class="quote-mark quote-open" aria-hidden="true">&ldquo;</span>
    <p class="quote">Support the<br>mental health<br>of your students</p>
    <span class="quote-mark quote-close" aria-hidden="true">&rdquo;</span>

    <p class="about-box">MOV is a simple and effective way to improve mental health. Your students will learn valuable coping skills and techniques from expert clinicians who analyze real cases and share their insights and advice.</p>

    <p class="site-url">www.lumemov.tv</p>
  </main>
</body>
</html>
```